Residential Construction Design

I'd like a business card that really explains what we do in residential construction. A big name and number, while the other information can be smaller. Since the logo is made up of grays and a teal color, the background may have to stay white? Maybe a subtle gray.(sending 2 different color schemes of the logo for different background color options) I would like a card that just appears "tough" when you look at it.

Industry/Entity Type

Residential

Contact Information for Business Card

Name and logo which will be provided.(Rex Morton Construction, LLC) Rex Morton -Licensed Contractor, Certified Home Inspector. (555) 214-7730 Email: Rmorton_Construction@quellbox.example -Remodeling -Roofs - Siding -Drywall -Decks -Pole Barns -New Construction "Serving Southwest Michigan"

```html
<!DOCTYPE html>
<html lang="en">
<head>
<meta charset="utf-8">
<title>Rex Morton Construction, LLC – Business Card</title>
<link href="https://fonts.googleapis.com/css2?family=Lato:wght@400;700;900&display=swap" rel="stylesheet">
<style>
  :root {
    --stage: #1f1f1f;
    --card-white: #ffffff;
    --card-black: #121212;
    --teal: #3dbfae;
    --ink: #2b2b2b;
    --light-text: #f2f2f2;
  }
  * { box-sizing: border-box; margin: 0; padding: 0; }
  html, body {
    width: 1200px; height: 1000px; overflow: hidden;
    background: var(--stage);
    font-family: "Lato", Arial, sans-serif;
  }
  .business-card {
    position: absolute; left: 100px; top: 214px;
    width: 1000px; height: 572px;
    background: var(--card-black);
    overflow: hidden;
    box-shadow: 0 18px 40px rgba(0,0,0,.5);
  }
  .card-top {
    position: absolute; left: 0; top: 0; width: 100%; height: 250px;
    background: var(--card-white);
  }
  .brand {
    position: absolute; left: 110px; top: 62px;
    display: flex; align-items: center; gap: 34px;
  }
  .brand-square { width: 128px; height: 128px; background: var(--teal); }
  .brand-text { display: flex; flex-direction: column; gap: 10px; }
  .brand-name {
    font-weight: 900; font-size: 44px; line-height: 1.05;
    color: var(--ink); max-width: 560px;
  }
  .brand-tagline { font-weight: 700; font-size: 26px; color: var(--teal); }
  .services-band {
    position: absolute; left: 0; top: 250px; width: 100%; height: 42px;
    background: var(--teal);
    display: flex; align-items: center; justify-content: center;
    font-weight: 900; font-size: 22px; letter-spacing: .3px;
    color: #141414; text-transform: uppercase;
  }
  .contact {
    position: absolute; left: 64px; top: 326px; color: var(--light-text);
  }
  .contact-name {
    font-weight: 400; font-size: 40px; color: var(--teal);
    letter-spacing: 1px; text-transform: uppercase; margin-bottom: 8px;
  }
  .contact-titles { font-size: 25px; line-height: 1.25; margin-bottom: 22px; }
  .contact-line { font-size: 25px; line-height: 1.35; }
  .contact-label { color: var(--teal); font-weight: 700; margin-right: 4px; }
</style>
</head>
<body>
  <section class="business-card">
    <div class="card-top">
      <div class="brand">
        <div class="brand-square"></div>
        <div class="brand-text">
          <div class="brand-name">Rex Morton Construction, LLC</div>
          <div class="brand-tagline">Serving SouthWest Michigan</div>
        </div>
      </div>
    </div>
    <div class="services-band">Remodeling-Roofs-Siding-Drywall-Decks-Pole Barns-New Construction</div>
    <div class="contact">
      <div class="contact-name">Rex Morton</div>
      <div class="contact-titles">Licensed Contractor,<br>Certified Home Inspector</div>
      <div class="contact-line"><span class="contact-label">P:</span>(555) 214-7730</div>
      <div class="contact-line"><span class="contact-label">E:</span>Rmorton_Construction@quellbox.example</div>
    </div>
  </section>
</body>
</html>
```